Tri fold flyer design for restoration company

Use our website for inspiration and make a world class advertising tri fold flyer.
harborlinerecovery.example

Colors
0054AA
0677BA
7BADD7
CADEEF
E8F1F8
00AB8E
00BBA5
67D7C9
C6EFE9
E9F9F6
EB3D1F
EC4F4E
F09395
F8D3D4
FCEDEE

```html
<!DOCTYPE html>
<html lang="en">
<head>
<meta charset="UTF-8">
<title>Harborline Recovery – Tri-fold Cover Panel</title>
<link rel="stylesheet" href="https://fonts.googleapis.com/css2?family=Open+Sans:wght@400;600&display=swap">
<style>
  :root {
    --stage: #e8f1f8;
    --panel-light: #f1f1f2;
    --panel-mid: #dcdde2;
    --panel-deep: #c9cad6;
    --brand-blue: #2c4f96;
    --wave-blue-start: #3a5e9e;
    --wave-blue-end: #1f3f86;
    --accent-orange: #e4532f;
    --accent-orange-deep: #c9401f;
    --white: #ffffff;
  }
  * { margin: 0; padding: 0; box-sizing: border-box; }
  html, body {
    width: 1200px;
    height: 900px;
    overflow: hidden;
    background: var(--stage);
    font-family: "Open Sans", sans-serif;
  }
  .canvas {
    position: relative;
    width: 1200px;
    height: 900px;
    display: flex;
    align-items: center;
    justify-content: center;
  }
  .cover-panel {
    position: relative;
    width: 400px;
    height: 860px;
    overflow: hidden;
    box-shadow: 0 10px 30px rgba(20, 50, 90, 0.18);
  }
  .panel-texture {
    position: absolute;
    inset: 0;
    background:
      radial-gradient(ellipse at 60% 22%, rgba(170,172,182,0.35), transparent 55%),
      linear-gradient(180deg, var(--panel-light) 0%, var(--panel-mid) 55%, var(--panel-deep) 100%);
  }
  .brand-name {
    position: absolute;
    top: 78px;
    left: 0;
    right: 0;
    text-align: center;
    font-size: 34px;
    font-weight: 600;
    color: var(--brand-blue);
    letter-spacing: 0.5px;
    line-height: 1.1;
  }
  .service-list {
    position: absolute;
    top: 400px;
    left: 0;
    right: 0;
    list-style: none;
    text-align: center;
    color: var(--accent-orange);
    font-size: 31px;
    font-weight: 400;
    line-height: 1.22;
  }
  .wave-footer {
    position: absolute;
    left: 0;
    bottom: 0;
    width: 400px;
    height: 280px;
    display: block;
  }
  .web-address {
    font-family: "Open Sans", sans-serif;
    font-size: 19px;
    letter-spacing: 1.4px;
    fill: var(--white);
  }
</style>
</head>
<body>
  <main class="canvas">
    <section class="cover-panel">
      <div class="panel-texture" role="img" aria-label="Light grey weathered concrete texture background"></div>

      <h1 class="brand-name">Harborline Recovery</h1>

      <ul class="service-list">
        <li>Water Damage</li>
        <li>Fire Damage</li>
        <li>Mold Remediation</li>
      </ul>

      <svg class="wave-footer" viewBox="0 0 400 280" aria-hidden="false">
        <defs>
          <linearGradient id="waveBlue" x1="0" y1="0" x2="1" y2="1">
            <stop offset="0" stop-color="var(--wave-blue-start)"/>
            <stop offset="1" stop-color="var(--wave-blue-end)"/>
          </linearGradient>
          <linearGradient id="waveOrange" x1="0" y1="0" x2="1" y2="0">
            <stop offset="0" stop-color="var(--accent-orange)"/>
            <stop offset="1" stop-color="var(--accent-orange-deep)"/>
          </linearGradient>
        </defs>
        <path d="M0 160 C110 120 250 40 400 10 L400 60 C250 95 110 170 0 215 Z" fill="url(#waveOrange)"/>
        <path d="M0 198 C110 158 250 80 400 44 L400 280 L0 280 Z" fill="url(#waveBlue)"/>
        <text class="web-address" x="200" y="246" text-anchor="middle">www.harborlinerecovery.example</text>
      </svg>
    </section>
  </main>
</body>
</html>
```